Wordpress Template for Food Retail Shop

We need a wordpress template that fits our new wp installation with about 6-7 sites. frontpage, news, team, products, contact. we provide food from local suppliers, * green * products. we provide a local bakery

```html
<!DOCTYPE html>
<html lang="en">
<head>
<meta charset="utf-8">
<title>Verdelle Bakery</title>
<link href="https://fonts.googleapis.com/css2?family=Open+Sans:wght@400;600;700;800&display=swap" rel="stylesheet">
<style>
:root{
  --green:#8cc63f;
  --orange:#f7a823;
  --dark:#2e2e2e;
  --darker:#232323;
  --text:#6b6b6b;
  --heading:#333333;
  --line:#e4e4e4;
  --white:#ffffff;
}
*{margin:0;padding:0;box-sizing:border-box}
html,body{width:1200px;height:3972px;overflow:hidden}
body{font-family:"Open Sans",Arial,sans-serif;color:var(--text);background:var(--white);position:relative}
a{color:inherit;text-decoration:none}
.abs{position:absolute}

/* header */
.site-header{position:absolute;left:0;top:0;width:1200px;height:72px;background:var(--white)}
.brand{position:absolute;left:80px;top:20px;display:flex;align-items:center;gap:8px;font-weight:800;font-size:26px;color:var(--green);letter-spacing:1px}
.brand-dot{width:22px;height:22px;border-radius:50%;background:var(--green)}
.main-nav{position:absolute;left:322px;top:26px;display:flex;gap:56px;font-size:14px;font-weight:600;color:#444}
.header-tools{position:absolute;right:80px;top:22px;display:flex;gap:22px;align-items:center;font-size:12px;color:#555}

/* buttons */
.btn{display:inline-block;background:var(--orange);color:var(--white);font-size:13px;font-weight:700;border-radius:20px;padding:9px 26px;text-transform:uppercase}
.btn-green{background:var(--green)}

/* hero */
.hero{position:absolute;left:0;top:72px;width:1200px;height:588px;background:linear-gradient(100deg,#4a2d1c 0%,#6b4128 35%,#3a2214 60%,#7b5a3e 100%)}
.hero-title{position:absolute;left:70px;top:250px;color:var(--white);font-weight:800;font-size:54px;line-height:58px}
.hero-sub{position:absolute;left:70px;top:384px;color:#f1e6da;font-size:13px}
.hero .btn{position:absolute;left:70px;top:428px}
.dots{display:flex;gap:8px}
.dots span{width:10px;height:10px;border-radius:50%;background:rgba(255,255,255,.55)}
.dots span.on{background:var(--white)}

/* section titles */
.section-title{position:absolute;left:0;width:1200px;text-align:center;font-size:30px;font-weight:700;color:var(--heading)}
.title-rule{position:absolute;left:576px;width:48px;height:3px;background:var(--green)}

/* products */
.products{position:absolute;left:80px;top:800px;width:1040px;height:410px;display:flex}
.product{flex:1;text-align:center;padding:0 22px;border-right:1px solid var(--line)}
.product:last-child{border-right:none}
.product-img{width:180px;height:140px;margin:0 auto 16px;border-radius:50%;background:radial-gradient(circle,#b06a2a 0%,#d89a52 55%,#fff 72%)}
.product h3{color:var(--green);font-size:18px;font-weight:700;margin-bottom:10px}
.product p{font-size:13px;line-height:19px;margin-bottom:14px}
.price{font-size:20px;color:#444;margin-bottom:14px}

/* banner */
.banner{position:absolute;left:0;top:1372px;width:1200px;height:408px;background:linear-gradient(90deg,#3d3023 0%,#4a3a2a 40%,#6f9f2a 55%,#8cc63f 100%)}
.banner-photo{position:absolute;left:660px;top:80px;width:330px;height:240px;border-radius:12px;background:linear-gradient(135deg,#5a3a1e,#8b6a44)}
.banner-kicker{position:absolute;left:80px;top:128px;color:var(--white);font-size:24px;font-weight:700}
.banner-title{position:absolute;left:80px;top:158px;color:var(--white);font-size:64px;font-weight:800}
.banner .btn{position:absolute;left:80px;top:250px}

/* team */
.team{position:absolute;left:80px;top:2026px;width:1040px;display:flex;justify-content:space-between}
.member{width:242px;text-align:center}
.member-photo{width:242px;height:310px;border:1px solid var(--line);background:linear-gradient(180deg,#f4f4f4,#dcdcdc)}
.member h3{margin-top:24px;color:var(--green);font-size:20px;font-weight:700}

/* testimonials */
.testimonials{position:absolute;left:0;top:2540px;width:1200px;height:400px;background:linear-gradient(180deg,#2c2520,#3a302a 50%,#1f1a17)}
.testimonials .section-title{color:var(--white);top:34px;font-size:28px}
.avatar{position:absolute;left:560px;top:92px;width:80px;height:80px;border-radius:50%;border:3px solid var(--orange);background:#a38468}
.quote{position:absolute;left:290px;top:196px;width:620px;text-align:center;color:#e4e4e4;font-size:14px;line-height:22px}
.quote-name{position:absolute;left:0;top:298px;width:1200px;text-align:center;color:var(--white);font-weight:700;font-size:16px}

/* news */
.news{position:absolute;left:80px;top:3086px;width:1040px;display:flex;justify-content:space-between}
.news-card{width:330px;border:1px solid var(--line);height:395px;position:relative}
.news-img{height:200px;background:linear-gradient(135deg,#c9b39a,#e8d6c4)}
.date{position:absolute;left:16px;top:0;width:52px;height:60px;background:var(--orange);color:var(--white);text-align:center;font-size:12px;font-weight:700;padding-top:10px;line-height:18px}
.news-body{padding:22px 24px}
.news-body h3{font-size:18px;color:var(--heading);font-weight:600;margin-bottom:10px}
.news-body p{font-size:13px;line-height:19px;margin-bottom:16px}
.read-more{color:var(--green);font-size:12px;font-weight:700;text-decoration:underline}

/* footer */
.site-footer{position:absolute;left:0;top:3600px;width:1200px;height:330px;background:var(--dark);color:#cfcfcf}
.footer-col{position:absolute;top:60px;font-size:13px;line-height:22px}
.footer-col h4{color:var(--white);font-size:20px;font-weight:700;margin-bottom:18px}
.footer-col ul{list-style:none}
.footer-col li{margin-bottom:4px}
.contact-row{display:flex;gap:10px;align-items:flex-start;margin-bottom:8px}
.news-input{width:236px;height:38px;border-radius:20px;background:var(--white);color:#999;font-size:12px;padding:10px 18px;margin-bottom:12px}
.bottom-bar{position:absolute;left:0;top:3930px;width:1200px;height:42px;background:var(--darker);color:#aaa;font-size:12px}
.bottom-bar p{position:absolute;left:80px;top:13px}
.social{position:absolute;right:80px;top:10px;display:flex;gap:8px}
.social span{width:22px;height:22px;border-radius:50%;background:var(--green)}
</style>
</head>
<body>

<header class="site-header">
  <div class="brand"><span class="brand-dot"></span>VERDELLE</div>
  <nav class="main-nav"><a>HOME</a><a>PRODUCTS</a><a>NEWS</a><a>TEAM</a><a>CONTACT US</a></nav>
  <div class="header-tools">
    <svg width="16" height="16" viewBox="0 0 16 16"><circle cx="7" cy="7" r="5" fill="none" stroke="#666" stroke-width="2"/><line x1="11" y1="11" x2="15" y2="15" stroke="#666" stroke-width="2"/></svg>
    <svg width="16" height="16" viewBox="0 0 16 16"><circle cx="8" cy="5" r="3.5" fill="none" stroke="#666" stroke-width="1.6"/><path d="M2 15c0-4 12-4 12 0" fill="none" stroke="#666" stroke-width="1.6"/></svg>
    <span>CART $0</span>
  </div>
</header>

<section class="hero" role="img" aria-label="Photo of a sliced chocolate cake on a wooden board">
  <h1 class="hero-title">DELICIOUS<br>CHOCOLATE CAKE</h1>
  <p class="hero-sub">Lorem Ipsum is simply dummy text of the printing and typesetting industry.</p>
  <a class="btn">Shop Now</a>
  <div class="dots abs" style="right:70px;top:540px"><span class="on"></span><span></span><span></span><span></span></div>
</section>

<h2 class="section-title" style="top:708px">NEW PRODUCTS IN BAKERY</h2>
<div class="title-rule" style="top:756px"></div>

<section class="products">
  <article class="product">
    <div class="product-img" role="img" aria-label="Blueberry muffin"></div>
    <h3>MUFFINS</h3>
    <p>Lorem Ipsum is simply dummy text of the printing and typesetting industry.</p>
    <div class="price">$15.99</div>
    <a class="btn">Shop Now</a>
  </article>
  <article class="product">
    <div class="product-img" role="img" aria-label="Round coffee cake"></div>
    <h3>COFFEE CAKE</h3>
    <p>Lorem Ipsum is simply dummy text of the printing and typesetting industry.</p>
    <div class="price">$15.99</div>
    <a class="btn">Shop Now</a>
  </article>
  <article class="product">
    <div class="product-img" role="img" aria-label="Golden croissant"></div>
    <h3>CROISSANT BREAD</h3>
    <p>Lorem Ipsum is simply dummy text of the printing and typesetting industry.</p>
    <div class="price">$15.99</div>
    <a class="btn">Shop Now</a>
  </article>
  <article class="product">
    <div class="product-img" role="img" aria-label="Chocolate tart"></div>
    <h3>CHOCOLATE TARTS</h3>
    <p>Lorem Ipsum is simply dummy text of the printing and typesetting industry.</p>
    <div class="price">$15.99</div>
    <a class="btn">Shop Now</a>
  </article>
</section>
<a class="btn btn-green abs" style="left:526px;top:1266px">Browse More</a>

<section class="banner" role="img" aria-label="Nut cake on a green leaf background">
  <div class="banner-photo" role="img" aria-label="Nut cake with a slice cut out"></div>
  <p class="banner-kicker">NEW ARRIVAL IN BAKERY</p>
  <h2 class="banner-title">NUT CAKE</h2>
  <a class="btn">Shop Now</a>
</section>

<h2 class="section-title" style="top:1910px">OUR TEAM</h2>
<div class="title-rule" style="top:1958px"></div>
<section class="team">
  <div class="member"><div class="member-photo" role="img" aria-label="Chef in white uniform"></div><h3>OWEN HALE</h3></div>
  <div class="member"><div class="member-photo" role="img" aria-label="Chef in white uniform"></div><h3>PETER LIND</h3></div>
  <div class="member"><div class="member-photo" role="img" aria-label="Chef in white uniform"></div><h3>CLARA MOSS</h3></div>
  <div class="member"><div class="member-photo" role="img" aria-label="Chef in white uniform"></div><h3>TOMAS</h3></div>
</section>
<a class="btn abs" style="left:536px;top:2450px">View More</a>

<section class="testimonials" role="img" aria-label="Dark blurred bakery photo background">
  <h2 class="section-title">OUR CLIENTS SAY`S</h2>
  <div class="avatar" role="img" aria-label="Client portrait"></div>
  <p class="quote">“ Lorem Ipsum is simply dummy text of the printing and typesetting industry. Lorem Ipsum has been the industry's standard dummy text ever since the 1500s, when an unknown printer took a galley of type and scrambled it to make a type specimen book. ”</p>
  <p class="quote-name">RAVEL TINSDORF</p>
  <div class="dots abs" style="left:573px;top:336px"><span class="on"></span><span></span><span></span></div>
</section>

<h2 class="section-title" style="top:2980px">LATEST NEWS</h2>
<div class="title-rule" style="top:3028px"></div>
<section class="news">
  <article class="news-card">
    <div class="news-img" role="img" aria-label="Hands decorating cupcakes"></div>
    <div class="date">20<br>MAY</div>
    <div class="news-body"><h3>News Heading</h3><p>Lorem Ipsum is simply dummy text of the printing and typesetting industry. Lorem Ipsum has been the industry's standard dummy text ever since the 1500s.</p><a class="read-more">READ MORE</a></div>
  </article>
  <article class="news-card">
    <div class="news-img" role="img" aria-label="Baker working in a kitchen"></div>
    <div class="date">20<br>MAY</div>
    <div class="news-body"><h3>News Heading</h3><p>Lorem Ipsum is simply dummy text of the printing and typesetting industry. Lorem Ipsum has been the industry's standard dummy text ever since the 1500s.</p><a class="read-more">READ MORE</a></div>
  </article>
  <article class="news-card">
    <div class="news-img" role="img" aria-label="Shelves of fresh bread loaves"></div>
    <div class="date">20<br>MAY</div>
    <div class="news-body"><h3>News Heading</h3><p>Lorem Ipsum is simply dummy text of the printing and typesetting industry. Lorem Ipsum has been the industry's standard dummy text ever since the 1500s.</p><a class="read-more">READ MORE</a></div>
  </article>
</section>
<a class="btn btn-green abs" style="left:526px;top:3518px">Browse More</a>

<footer class="site-footer">
  <div class="footer-col" style="left:80px;width:300px">
    <div class="brand" style="position:static;margin-bottom:20px"><span class="brand-dot"></span>VERDELLE</div>
    <p>Lorem Ipsum is simply dummy text of the printing and typesetting industry. Lorem Ipsum has been the industry's standard dummy text.</p>
    <p style="margin-top:14px;color:var(--green);font-weight:700;text-decoration:underline">READ MORE...</p>
  </div>
  <div class="footer-col" style="left:440px">
    <h4>QUICK LINKS</h4>
    <ul><li>Home</li><li>Products</li><li>News</li><li>Team</li><li>Contact us</li></ul>
  </div>
  <div class="footer-col" style="left:625px;width:220px">
    <h4>CONTACT INFO</h4>
    <div class="contact-row"><svg width="14" height="14" viewBox="0 0 14 14"><path d="M3 1l2 3-1.5 1.5a7 7 0 0 0 5 5L10 9l3 2-1 2.5C6 13 1 8 .5 2z" fill="#8cc63f"/></svg><span>+000 123 4567</span></div>
    <div class="contact-row"><svg width="14" height="14" viewBox="0 0 14 14"><rect x="1" y="3" width="12" height="8" fill="none" stroke="#8cc63f" stroke-width="1.5"/><path d="M1 3l6 5 6-5" fill="none" stroke="#8cc63f" stroke-width="1.5"/></svg><span>hello@verdelle.test</span></div>
    <div class="contact-row"><svg width="14" height="14" viewBox="0 0 14 14"><path d="M7 1a4.5 4.5 0 0 0-4.5 4.5C2.5 9 7 13 7 13s4.5-4 4.5-7.5A4.5 4.5 0 0 0 7 1z" fill="#8cc63f"/><circle cx="7" cy="5.5" r="1.6" fill="#2e2e2e"/></svg><span>12 Meadow Lane<br>Greenfield, ST 00000</span></div>
  </div>
  <div class="footer-col" style="left:884px">
    <h4>NEWSLETTER</h4>
    <div class="news-input">Email Address</div>
    <a class="btn btn-green" style="width:236px;text-align:center">Subscribe</a>
  </div>
</footer>
<div class="bottom-bar">
  <p>Copyright © 2024 Verdelle Bakery. All Rights Reserved.</p>
  <div class="social"><span></span><span></span><span></span><span></span><span></span><span></span></div>
</div>

</body>
</html>
```